Exercise Physiologist needs business cards

I have a logo, I need business cards (Sole trader) as I am moving to a new location and would like an updated look. I provide gym based exercise rehabilitation, injury prevention and movement assessments. I have over 13 years experience as an Exercise Physiologist. I would like the cards to look professional but not boring and can be a little different to stand out when sitting with other Allied Health Professional cards.

Target Market(s)

GP's, Allied health practitioners, people with injuries wanting to exercise

Industry/Entity Type

Health And Wellness

Contact Information for Business Card

Megan Trowbridge - Exercise Physiologist 0487 926 350
52 Wattlebird Lane
Kellmore East
(Gate 4, Brennock Fitness)
vornalhealth@mailbox-example.com
facebook.com/Vornal

Requirements
Must have
• I would like to include a section to add next appointment date and time space to the back of the card.
Nice to have
• Rounded corners and a black background on 1 or 2 sides.
Should not have
• Pictures of fit/toned bodies etc

```html
<!DOCTYPE html>
<html lang="en">
<head>
<meta charset="utf-8">
<title>Vornal Health – Business Cards</title>
<link rel="stylesheet" href="https://fonts.googleapis.com/css2?family=Oswald:wght@300;400;500;600&display=swap">
<style>
  :root {
    --bg: #1e1f22;
    --card: #ffffff;
    --blue: #2c5fbf;
    --blue-deep: #214c9e;
    --blue-light: #5aa8e0;
    --circle-fill: #cfe6f7;
    --ink: #2d2f33;
    --ink-soft: #5a5e66;
    --dots: #eef0f3;
    --rule: #9fb4d6;
  }
  * { box-sizing: border-box; margin: 0; padding: 0; }
  html, body {
    width: 1200px; height: 900px; overflow: hidden;
    background: var(--bg);
    font-family: "Oswald", "Arial Narrow", sans-serif;
  }
  .canvas { position: relative; width: 1200px; height: 900px; }

  .card {
    position: absolute;
    top: 286px;
    width: 540px; height: 327px;
    background: var(--card);
    border-radius: 24px;
    overflow: hidden;
  }
  .card--back { left: 40px; }
  .card--front { left: 620px; }

  /* Shared brand lockup */
  .brand { position: absolute; display: flex; align-items: center; gap: 12px; }
  .brand__mark {
    width: 62px; height: 62px; border-radius: 50%;
    background: var(--blue-light);
  }
  .brand__name {
    font-weight: 400; font-size: 46px; line-height: 1;
    color: var(--blue);
    letter-spacing: 0.5px;
  }

  /* Front */
  .front__band { position: absolute; left: 0; top: 0; }
  .front__identity {
    position: absolute; right: 30px; top: 20px;
    text-align: right; color: #fff;
  }
  .front__name {
    font-weight: 500; font-size: 31px; letter-spacing: 1.5px;
    text-transform: uppercase; line-height: 1.1;
  }
  .front__role {
    font-weight: 400; font-size: 13px; letter-spacing: 1.2px;
    text-transform: uppercase;
  }
  .front .brand { left: 34px; top: 152px; }
  .front__contact {
    position: absolute; left: 340px; top: 140px;
    font-weight: 300; font-size: 15px; line-height: 1.45;
    color: var(--ink); text-transform: uppercase; letter-spacing: 0.6px;
    list-style: none;
  }
  .front__contact .phone { margin-bottom: 10px; }

  /* Back */
  .back__heading {
    position: absolute; left: 30px; top: 22px;
    text-transform: uppercase; line-height: 1;
  }
  .back__heading-next {
    display: block; font-weight: 600; font-size: 24px;
    letter-spacing: 4px; color: var(--blue-light);
  }
  .back__heading-main {
    display: block; font-weight: 600; font-size: 32px;
    letter-spacing: 3px; color: var(--blue-deep); margin-top: 4px;
  }
  .back .brand { left: 300px; top: 36px; }
  .back__stripe-thick {
    position: absolute; left: 0; top: 122px; width: 100%; height: 9px;
    background: var(--blue);
  }
  .back__stripe-thin {
    position: absolute; left: 0; top: 136px; width: 100%; height: 2px;
    background: var(--blue);
  }
  .back__texture {
    position: absolute; left: 0; top: 138px; width: 100%; height: 165px;
    background: var(--dots);
  }
  .back__footer-band {
    position: absolute; left: 0; bottom: 0; width: 100%; height: 24px;
    background: var(--blue);
  }

  .days {
    position: absolute; left: 50px; top: 156px; width: 440px;
    display: flex; justify-content: space-between; list-style: none;
  }
  .day { display: flex; flex-direction: column; align-items: center; gap: 5px; }
  .day__box {
    width: 24px; height: 24px; border-radius: 50%;
    background: var(--circle-fill);
    border: 3px solid var(--blue);
  }
  .day__label {
    font-weight: 400; font-size: 11px; letter-spacing: 0.8px;
    color: var(--ink); text-transform: uppercase;
  }

  .when {
    position: absolute; left: 30px; right: 30px; top: 246px;
    display: flex; align-items: flex-end; gap: 10px;
    font-weight: 400; font-size: 13px; letter-spacing: 1px;
    color: var(--ink); text-transform: uppercase;
  }
  .when__line { flex: 1; height: 1px; background: var(--rule); margin-bottom: 4px; }
</style>
</head>
<body>
<main class="canvas">

  <section class="card card--back back" aria-label="Appointment side">
    <h2 class="back__heading">
      <span class="back__heading-next">Next</span>
      <span class="back__heading-main">Appointment</span>
    </h2>
    <div class="brand">
      <span class="brand__mark"></span>
      <span class="brand__name">Vornal</span>
    </div>
    <div class="back__stripe-thick"></div>
    <div class="back__stripe-thin"></div>
    <div class="back__texture" role="img" aria-label="Soft grey halftone dot pattern behind the appointment fields"></div>
    <ul class="days">
      <li class="day"><span class="day__box"></span><span class="day__label">Mon</span></li>
      <li class="day"><span class="day__box"></span><span class="day__label">Tue</span></li>
      <li class="day"><span class="day__box"></span><span class="day__label">Wed</span></li>
      <li class="day"><span class="day__box"></span><span class="day__label">Thu</span></li>
      <li class="day"><span class="day__box"></span><span class="day__label">Fri</span></li>
      <li class="day"><span class="day__box"></span><span class="day__label">Sat</span></li>
    </ul>
    <div class="when">
      <span>Date</span><span class="when__line"></span>
      <span>Time</span><span class="when__line"></span>
      <span>PM/AM</span>
    </div>
    <div class="back__footer-band"></div>
  </section>

  <section class="card card--front front" aria-label="Contact side">
    <svg class="front__band" width="540" height="116" viewBox="0 0 540 116" aria-hidden="true">
      <defs>
        <linearGradient id="bandTone" x1="0" y1="0" x2="1" y2="1">
          <stop offset="0" stop-color="#2f64c4"/>
          <stop offset="1" stop-color="#2556b0"/>
        </linearGradient>
      </defs>
      <polygon points="0,0 540,0 540,96 416,96 398,115 380,96 0,96" fill="url(#bandTone)"/>
    </svg>
    <div class="front__identity">
      <h1 class="front__name">Megan Trowbridge</h1>
      <p class="front__role">Exercise Physiologist</p>
    </div>
    <div class="brand">
      <span class="brand__mark"></span>
      <span class="brand__name">Vornal</span>
    </div>
    <ul class="front__contact">
      <li class="phone">0487 926 350</li>
      <li>52 Wattlebird Lane</li>
      <li>Kellmore East</li>
      <li>(Gate 4, Brennock Fitness)</li>
    </ul>
  </section>

</main>
</body>
</html>
```